Silver Kettle Studio Marketing Postcard

I need a 2 sided A6 postcard to distribute to potential clients. The postcard will include the business logo and information about the service we provide and contact information. I want it to be stylish and to compliment the business card. I've attached the business card and logo files as well as some text to use. I have other source files (.eps and.ai) if required please message me. I don't need the postal address or my position included on the postcard.
I am open to portrait or landscape designs, whatever you think is most stylish and eye catching.

```html
<!DOCTYPE html>
<html lang="en">
<head>
<meta charset="utf-8">
<title>Silver Kettle Studio – Postcard</title>
<link href="https://fonts.googleapis.com/css2?family=Noto+Sans:wght@400;700&display=swap" rel="stylesheet">
<style>
  :root {
    --backdrop: #e8e5df;
    --leaf-green: #7db143;
    --night-navy: #082639;
    --white: #ffffff;
    --body-font: "Noto Sans", Verdana, sans-serif;
  }
  * { margin: 0; padding: 0; box-sizing: border-box; }
  html, body {
    width: 857px;
    height: 1200px;
    overflow: hidden;
    background: var(--backdrop);
    font-family: var(--body-font);
  }
  .canvas {
    position: relative;
    width: 857px;
    height: 1200px;
  }
  .postcard {
    position: absolute;
    left: 52px;
    width: 757px;
    height: 536px;
    overflow: hidden;
  }
  /* Front side */
  .postcard--front {
    top: 35px;
    background: var(--leaf-green);
    color: var(--white);
  }
  .brand-name {
    position: absolute;
    left: 0;
    right: 0;
    top: 215px;
    text-align: center;
    font-size: 52px;
    font-weight: 400;
    letter-spacing: 1px;
    color: var(--white);
  }
  .tagline {
    position: absolute;
    left: 0;
    right: 0;
    top: 469px;
    text-align: center;
    font-size: 20px;
    font-weight: 700;
  }
  /* Back side */
  .postcard--back {
    top: 613px;
    background: var(--night-navy);
    color: var(--white);
  }
  .back-shapes {
    position: absolute;
    inset: 0;
  }
  .service-info {
    position: absolute;
    left: 40px;
    width: 407px;
    top: 78px;
    text-align: right;
    font-size: 15.5px;
    line-height: 1.45;
  }
  .headline {
    color: var(--leaf-green);
    font-size: 19px;
    font-weight: 700;
    line-height: 1.25;
  }
  .subheadline {
    color: var(--leaf-green);
    font-size: 15.5px;
    font-weight: 700;
    margin-bottom: 14px;
  }
  .service-info p { margin-bottom: 14px; }
  .highlight { color: var(--leaf-green); font-weight: 700; }
  .service-list {
    color: var(--leaf-green);
    font-weight: 700;
    margin-top: -14px;
  }
  .contact {
    position: absolute;
    left: 46px;
    top: 395px;
    width: 560px;
    font-size: 15.5px;
    line-height: 1.45;
  }
  .contact-lead {
    color: var(--leaf-green);
    font-weight: 700;
    margin-bottom: 12px;
  }
</style>
</head>
<body>
<main class="canvas">

  <section class="postcard postcard--front">
    <div class="brand-name">Silver Kettle Studio</div>
    <p class="tagline">Helping you navigate this Digital Life</p>
  </section>

  <section class="postcard postcard--back">
    <svg class="back-shapes" width="757" height="536" viewBox="0 0 757 536" aria-hidden="true">
      <path d="M757 0 C700 90 610 230 625 536 L757 536 Z" fill="var(--leaf-green)"/>
      <path d="M0 412 A40 40 0 0 1 34 412 L0 460 Z" fill="var(--leaf-green)"/>
    </svg>

    <div class="service-info">
      <div class="headline">Technology explained.</div>
      <div class="subheadline">Problems Solved.</div>
      <p>Do you feel frustrated by computers, TVs, phones, tablets and countless other digital devices?<br>
        <span class="highlight">Silver Kettle Studio</span> is here to help.</p>
      <p>From a simple computer health check to the purchase and installation of home networks and digital services.</p>
      <p>We also give useful product advice and maintenance tips:</p>
      <p class="service-list">On site support | Advice | Installation | Education</p>
    </div>

    <div class="contact">
      <p class="contact-lead">Let us help you tame your digital world.</p>
      <p>Phone conversations are free so call Rowan on 0400 555 318,
        email info@silverkettlestudio.com.au or go to www.silverkettlestudio.com.au
        for more information. Problems Solved.</p>
    </div>
  </section>

</main>
</body>
</html>
```